Sandwich board

We are a Photo booth company in NZ.
We need a sandwich board design we have all the guts and we know the style we want just need help making it look good/right.
Dimension of the board are 59cm by 69cm.
The other side is a chalk board so we can write about the event we are at.
The board is a light white wash ply and we will be applying by stencil or dye cut vinyl.
The words are
Just grab a prop
and strike a pose
take your own
black and white or colour
photos
And a carriage with a camera in the back.

Reason: I would like to see a bit more of a play around with the fonts and style.

Target Market(s)

this will be at event mostly weddings, birthdays, fairs really any event.

Industry/Entity Type

Camera

Requirements
Must have
• it must be black with white back ground
Nice to have
• simple lines
Should not have
• colour. to much little detail.

```html
<!DOCTYPE html>
<html lang="en">
<head>
<meta charset="utf-8">
<title>Grab a Prop – Sandwich Board</title>
<link rel="stylesheet" href="https://fonts.googleapis.com/css2?family=Bebas+Neue&family=Lobster&family=Montserrat:wght@800&family=Open+Sans:wght@400&family=PT+Sans+Narrow&family=Roboto+Condensed:wght@700&family=Rye&display=swap">
<style>
  :root {
    --ink: #111111;
    --paper: #ffffff;
    --ornament-tone: #8a8a8a;
    --ornament-tone-light: #c9c9c9;
  }
  * { margin: 0; padding: 0; box-sizing: border-box; }
  html, body { width: 1026px; height: 1200px; overflow: hidden; background: var(--paper); }
  .board { position: relative; width: 1026px; height: 1200px; background: var(--paper); color: var(--ink); }
  .frame { position: absolute; inset: 0; }
  .ornament {
    position: absolute;
    background: linear-gradient(180deg, var(--ornament-tone), var(--ornament-tone-light));
    border-radius: 6px;
  }
  .ornament--tl { left: 38px; top: 14px; width: 62px; height: 210px; }
  .ornament--tr { left: 924px; top: 14px; width: 62px; height: 210px; }
  .ornament--bl { left: 38px; top: 912px; width: 62px; height: 252px; }
  .ornament--br { left: 924px; top: 912px; width: 62px; height: 252px; }
  .ornament--ml { left: 52px; top: 250px; width: 34px; height: 34px; }
  .ornament--mr { left: 938px; top: 250px; width: 34px; height: 34px; }

  .banner { position: absolute; left: 366px; top: 70px; width: 278px; height: 106px; }
  .headline { position: absolute; left: 0; width: 1026px; text-align: center; white-space: nowrap; }
  .headline--grab {
    top: 164px; left: 228px; width: 580px;
    font-family: "Bebas Neue", sans-serif; font-size: 128px; line-height: 1; letter-spacing: 2px;
  }
  .headline--and {
    position: absolute; left: 258px; top: 284px; width: 22px;
    font-family: "Open Sans", sans-serif; font-size: 27px; line-height: 26px; text-align: center;
  }
  .headline--strike {
    top: 262px; left: 284px; width: 494px; text-align: left;
    font-family: "Lobster", cursive; font-size: 106px; line-height: 1.05;
  }
  .headline--pose {
    top: 358px; left: 274px; width: 472px;
    font-family: "Montserrat", sans-serif; font-weight: 800; font-size: 136px; line-height: 1.05; letter-spacing: -2px;
  }
  .divider { position: absolute; left: 167px; top: 503px; width: 700px; height: 4px; background: var(--ink); }
  .kicker {
    position: absolute; left: 352px; top: 536px;
    font-family: "Open Sans", sans-serif; font-size: 28px; letter-spacing: -0.5px;
  }
  .options { position: absolute; top: 568px; left: 0; width: 1026px; height: 110px;
    font-family: "PT Sans Narrow", sans-serif; font-size: 104px; line-height: 1; }
  .options span { position: absolute; top: 0; white-space: nowrap; }
  .options .connector { font-family: "Rye", serif; font-size: 24px; line-height: 22px; top: 22px; text-align: center; width: 50px; }
  .opt-black { left: 84px; }
  .opt-and { left: 318px; }
  .opt-white { left: 372px; }
  .opt-or { left: 636px; }
  .opt-colour { left: 688px; }
  .photos {
    position: absolute; left: 216px; top: 710px;
    font-family: "Open Sans", sans-serif; font-size: 92px; line-height: 1.1;
  }
  .carriage {
    position: absolute; left: 333px; top: 824px; width: 380px; height: 264px;
    background: linear-gradient(180deg, #5a5a5a, #9a9a9a);
    border-radius: 8px;
  }
  .contact {
    position: absolute; left: 0; top: 1098px; width: 1026px; text-align: center;
    font-family: "Roboto Condensed", sans-serif; font-weight: 700; font-size: 50px; line-height: 1.1;
    padding-right: 30px;
  }
</style>
</head>
<body>
<main class="board">
  <svg class="frame" width="1026" height="1200" viewBox="0 0 1026 1200" aria-hidden="true">
    <line x1="69" y1="42" x2="955" y2="42" stroke="#111" stroke-width="3"/>
    <line x1="69" y1="42" x2="69" y2="1140" stroke="#111" stroke-width="3"/>
    <line x1="955" y1="42" x2="955" y2="1140" stroke="#111" stroke-width="3"/>
  </svg>

  <div class="ornament ornament--tl" role="img" aria-label="Victorian scroll corner ornament"></div>
  <div class="ornament ornament--tr" role="img" aria-label="Victorian scroll corner ornament"></div>
  <div class="ornament ornament--ml" role="img" aria-label="Small fleuron on the frame line"></div>
  <div class="ornament ornament--mr" role="img" aria-label="Small fleuron on the frame line"></div>
  <div class="ornament ornament--bl" role="img" aria-label="Victorian scroll corner ornament"></div>
  <div class="ornament ornament--br" role="img" aria-label="Victorian scroll corner ornament"></div>

  <svg class="banner" viewBox="0 0 278 106" aria-hidden="false">
    <path d="M0 20 L46 26 L46 80 L10 86 L24 56 Z" fill="#111"/>
    <path d="M278 6 L232 16 L232 70 L268 62 L254 36 Z" fill="#111"/>
    <path d="M34 22 Q140 44 246 6 L246 66 Q140 104 34 82 Z" fill="#111"/>
    <text x="140" y="78" text-anchor="middle" font-family="Bebas Neue, sans-serif" font-size="62"
          fill="#fff" letter-spacing="4" transform="rotate(-6 140 60)">JUST</text>
  </svg>

  <h1 class="headline headline--grab">GRAB A PROP</h1>
  <div class="headline--and">a<br>n<br>d</div>
  <p class="headline headline--strike">Strike a</p>
  <p class="headline headline--pose">POSE!</p>

  <div class="divider"></div>

  <p class="kicker">TAKE YOUR OWN</p>
  <p class="options">
    <span class="opt-black">Black</span>
    <span class="connector opt-and">AND</span>
    <span class="opt-white">White</span>
    <span class="connector opt-or">OR</span>
    <span class="opt-colour">Colour</span>
  </p>
  <p class="photos">photos</p>

  <div class="carriage" role="img" aria-label="Engraved horse-drawn carriage with a large bellows camera in the back"></div>

  <p class="contact">Call 000 000 0000 for details</p>
</main>
</body>
</html>
```